Logo-Design für Oldtimerhandel Wendrat&Wendrat klassische Automobile OG
Zielgruppe
Handel mit Oldtimern, speziell aus den 60er und 70er Jahren. Zielgruppe sind überwiegend Menschen, die sich von der Masse abheben möchten und Wert auf etwas Einzigartiges legen.
Aufgabenstellung
Das Design soll ein hochwertiges Gesamterscheinungsbild mit gutem Wiedererkennungswert haben. Auch kann ein stilisierter Oldtimer Teil des Logos sein, um für die Zielgruppe besser erkennbar zu sein.
Das Logo muss für Homepage, Visitkarten, Briefpapier etc. tauglich sein und auch in S/W gut erkennbar sein können. Ebenso sollte es möglich sein, Autos mit dem Logo bzw. Schriftzug zu branden.
Beispielhaft wäre das Logo bzw. der Internetauftritt von http://www.harmsdorf-vintage-motors.example vergleichbar.

```html
<!DOCTYPE html>
<html lang="de">
<head>
<meta charset="utf-8">
<title>Wendrat &amp; Wendrat – Geschäftsausstattung</title>
<link href="https://fonts.googleapis.com/css2?family=Jost:wght@400;500&display=swap" rel="stylesheet">
<style>
:root{
  --bg:#efefef;
  --paper:#ffffff;
  --gold:#c3893a;
  --accent:#c27a35;
  --grey:#b1b1b1;
  --ink:#2b2b2b;
  --label:#7a7a7a;
  --line:#9a9a9a;
}
*{margin:0;padding:0;box-sizing:border-box}
html,body{width:1200px;height:801px;overflow:hidden}
body{background:radial-gradient(ellipse at 40% 30%,#fafafa,var(--bg));font-family:"Jost",sans-serif;color:var(--ink);position:relative}
.abs{position:absolute}
.sheet{background:var(--paper);box-shadow:0 6px 14px rgba(0,0,0,.18)}
.wordmark{color:var(--gold);font-weight:500;line-height:.95;text-align:left;white-space:nowrap;text-transform:uppercase}
.wordmark .l2{display:block;padding-left:1.35em}
.wordmark .sub{display:block;padding-left:1.6em;letter-spacing:.3em;font-size:.36em;margin-top:.25em;line-height:1}
.logo-main{left:202px;top:90px;font-size:34px}
.label{font-size:15px;color:var(--label);font-weight:400;transform:translateX(-50%)}
.card-front{left:58px;top:254px;width:259px;height:167px}
.card-front .wordmark{position:absolute;left:39px;top:69px;font-size:17px}
.card-back{left:333px;top:254px;width:259px;height:169px;overflow:hidden}
.card-back .name{position:absolute;left:36px;top:17px;color:var(--accent);font-variant:small-caps;font-size:17px;line-height:15px;letter-spacing:.03em}
.card-back .band{position:absolute;left:0;top:65px;width:100%;height:104px;background:var(--grey);color:#fff;font-variant:small-caps;padding:20px 36px;font-size:9px;line-height:13px;letter-spacing:.05em}
.card-back .band p+p{margin-top:8px}
.envelope{left:58px;top:496px;width:536px;height:267px}
.envelope .wordmark{position:absolute;left:52px;top:56px;font-size:11.5px}
.envelope .window{position:absolute;left:47px;top:121px;width:206px;height:111px;border-radius:12px;background:linear-gradient(135deg,#b9b9b9,#9d9d9d)}
.letter{left:630px;top:34px;width:521px;height:737px}
.letter .wordmark{position:absolute;left:376px;top:62px;font-size:10.5px}
.letter .contact{position:absolute;right:30px;top:143px;text-align:right;font-variant:small-caps;font-size:6.2px;line-height:10.5px;letter-spacing:.04em}
.letter .contact .acc{color:var(--accent)}
.letter .contact .gap{height:6px}
.letter .sender{position:absolute;left:62px;top:157px;font-variant:small-caps;font-size:5.4px;color:var(--accent);letter-spacing:.03em}
.letter .recipient{position:absolute;left:62px;top:170px;font-size:8px;line-height:12.3px}
.letter .subject{position:absolute;left:62px;top:246px;font-size:8px;font-weight:500}
.letter .body{position:absolute;left:62px;top:276px;width:425px;font-size:7.7px;line-height:10.5px}
.letter .body p{margin-bottom:10.5px}
.fold{position:absolute;left:0;width:11px;height:1px;background:var(--line)}
.letter .car-art{position:absolute;left:361px;top:619px;width:143px;height:55px;background:linear-gradient(90deg,#f4f4f4,#dcdcdc);border-radius:30px 30px 4px 4px}
.letter .rule{position:absolute;left:0;top:673px;width:100%;height:1px;background:var(--line)}
.letter .footer{position:absolute;top:689px;font-variant:small-caps;font-size:6.2px;line-height:10.5px;color:var(--accent);letter-spacing:.03em}
</style>
</head>
<body>

<div class="abs wordmark logo-main">Wendrat &amp;<span class="l2">Wendrat</span><span class="sub">Oldtimerhandel</span></div>

<div class="abs label" style="left:187px;top:224px">Visitenkarte vorne</div>
<div class="abs label" style="left:462px;top:224px">Visitenkarte hinten</div>

<div class="abs sheet card-front">
  <div class="wordmark">Wendrat &amp;<span class="l2">Wendrat</span><span class="sub">Oldtimerhandel</span></div>
</div>

<div class="abs sheet card-back">
  <div class="name">Max<br>Mustermann</div>
  <div class="band">
    <p>Musterstrasse 123<br>12345 Musterstadt<br>Tel.: 01234 567891</p>
    <p>musteremail@wendratundwendrat.example<br>www.wendratundwendrat.example</p>
  </div>
</div>

<div class="abs sheet envelope">
  <div class="wordmark">Wendrat &amp;<span class="l2">Wendrat</span><span class="sub">Oldtimerhandel</span></div>
  <div class="window"></div>
</div>

<div class="abs sheet letter">
  <div class="wordmark">Wendrat &amp;<span class="l2">Wendrat</span><span class="sub">Oldtimerhandel</span></div>
  <div class="contact">
    <div class="acc">Wendrat &amp; Wendrat</div>
    <div class="acc">Oldtimerhandel</div>
    <div>Musterstrasse 123</div>
    <div>12345 Musterstadt</div>
    <div class="gap"></div>
    <div>Telefon: 01234 567891</div>
    <div>Telefax: 01234 567812</div>
    <div class="gap"></div>
    <div>info@wendratundwendrat.example</div>
    <div>www.wendratundwendrat.example</div>
  </div>
  <div class="sender">Wendrat &amp; Wendrat | Musterstrasse 123 | 12345 Musterstadt</div>
  <div class="recipient">Frau Musterbeispiel<br>Musterstraße 3<br>48555 Muster</div>
  <div class="subject">Hier steht eine Betreffzeile</div>
  <div class="body">
    <p>Sehr geehrte Frau Musterbeispiel,</p>
    <p>als Kunde unseres jungen und modernen Unternehmens erwartet<br>Sie Qualität in höchstem Maße.</p>
    <p>Sie können sicher zu sein, genau zu bekommen, was wir Ihnen versprechen.<br>Und damit werden Sie auch rundum zufrieden sein. Das garantieren wir Ihnen.</p>
    <p>Schauen Sie doch gleich das beiliegende Prospekt. Wir bieten Ihnen moderne und hochwertige Produkte, die auf<br>dem neuesten Stand der Technik sind, an. Überzeugen Sie sich selbst von der hochwertigen Qualität unserer Produk-<br>te und bestellen Sie noch heute.</p>
    <p>Wir freuen uns auf Ihre Bestellung und sind bei Rückfragen gerne für Sie da.</p>
    <p>Mit freundlichen Grüßen</p>
  </div>
  <div class="fold" style="top:260px"></div>
  <div class="fold" style="top:368px"></div>
  <div class="fold" style="top:520px;background:var(--accent)"></div>
  <div class="car-art" role="img" aria-label="Linienzeichnung eines klassischen Sportwagens als Fußzeilendekor"></div>
  <div class="rule"></div>
  <div class="footer" style="left:62px">Wendrat &amp; Wendrat<br>Musterstrasse 123<br>12345 Musterstadt</div>
  <div class="footer" style="left:219px">USt-IdNr: DE000000000<br>Steuernummer: 000/000/000<br>Inhaber: Max Mustermann</div>
  <div class="footer" style="left:389px">Sparkasse Musterstadt<br>IBAN: DE00 0000 0000 0000 0000 00<br>BIC: MUSTDEXXX00</div>
</div>

</body>
</html>
```